Kaminari Martial Arts and Fitness Centre Flyer

My website is www.KaminariMartialArts.example.au

I am designing a 4 page flyer. I will use the flyer I have already prepared for me for the front page and I have a document I have prepared for the back page. See front page attachment.

I need you to produce pages 2 and 3, the two internal pages.

please check my website, any logos or photo you need let me know and I will upload them.

I want the theme to match the flyer I have see attachment front page.

Some possible things for inclusion:

Why choose Kaminari?
WELL KNOWN
We are Dunmore’s most popular martial arts school. Kaminari has a massive social media following right around the world. We regularly have instructors from Japan visiting our dojo.
WELL EQUIPPED
We have the largest and best equipped martial arts school in Australia. In fact, it is the best we have seen anywhere in the world.
WELL VERSED
We offer internationally recognised grades from some of the most prestigious and respected budo associations in the world. All of our black belt grades are registered in Japan.
WELL EXPERIENCED
The founder of Kaminari, Sensei Glen, has been training since 1987 and has well over 15000 hours of teaching experience behind him and has been awarded black belts in 9 different styles.

We have a comprehensive Stand Tall program that has been helping kids for well over a decade.

Choose from 80 classes a week.

QR code to my website timetable

Try a FREE lesson and receive a FREE uniform. Save up to $161.99

You don’t have to be great to start

over 80 classes a week to choose from
classes 6 days a week

internationally recognised grades

I also need a page which will be a timetable page.

On the page 4 leave a large blank section that I can add a timetable to later.

Target Market(s)

Families

Industry/Entity Type

Martial Arts

Colors
0054AA
0677BA
7BADD7
CADEEF
E8F1F8

Requirements
Must have
• project safe family friendly my corporate colours are black and blue

```html
<!DOCTYPE html>
<html lang="en">
<head>
<meta charset="utf-8">
<title>Why Choose Kaminari – Inside Spread</title>
<link href="https://fonts.googleapis.com/css2?family=Oswald:wght@600;700&family=Arimo:wght@400;700&display=swap" rel="stylesheet">
<style>
  :root {
    --stage: #98999c;
    --paper: #ffffff;
    --navy: #2f4684;
    --band: #364a80;
    --ink: #2b2b2b;
    --ink-soft: #333333;
    --mat-blue: #2f8fd6;
  }
  * { box-sizing: border-box; margin: 0; padding: 0; }
  html, body { width: 1200px; height: 914px; overflow: hidden; }
  body { background: var(--stage); font-family: "Arimo", Arial, sans-serif; color: var(--ink); position: relative; }

  .spread { position: absolute; left: 120px; top: 117px; width: 959px; height: 678px; background: var(--paper); overflow: hidden; }

  .heading-font { font-family: "Oswald", "Arial Narrow", sans-serif; font-weight: 700; text-transform: uppercase; }

  .main-title { position: relative; z-index: 2; position: absolute; left: 25px; top: 70px; font-size: 47px; line-height: 44px; color: var(--navy); letter-spacing: 0.5px; }

  .reason { position: absolute; left: 25px; width: 192px; z-index: 2; }
  .reason h3 { font-family: "Oswald", "Arial Narrow", sans-serif; font-weight: 700; font-size: 14.5px; line-height: 17px; color: var(--ink-soft); text-transform: uppercase; margin-bottom: 2px; }
  .reason p { font-size: 10.2px; line-height: 11.7px; color: var(--ink-soft); }
  .reason.known { top: 175px; }
  .reason.equipped { top: 269px; }
  .reason.versed { top: 351px; }
  .reason.experienced { top: 445px; }

  .photo { position: absolute; }
  .photo-founder { left: 232px; top: 13px; width: 272px; height: 580px; border-radius: 110px 110px 0 0; background: linear-gradient(180deg, #b9a9ad 0%, #e4b8c4 30%, #ee9fb3 60%, #f5c6d2 85%, #f9dbe3 100%); }
  .photo-thumb { left: 480px; width: 122px; height: 91px; }
  .photo-thumb.sparring { top: 91px; background: linear-gradient(180deg, #3a3c44 0%, #6b6e78 60%, #2a2b30 100%); }
  .photo-thumb.weapons { top: 218px; background: linear-gradient(180deg, #2d2f35 0%, #4a4d55 55%, var(--mat-blue) 100%); }
  .photo-thumb.grading { top: 390px; background: linear-gradient(180deg, #b9bcc2 0%, #e8e9ec 55%, var(--mat-blue) 100%); }
  .photo-circle { left: 785px; top: 185px; width: 213px; height: 213px; border-radius: 50%; background: radial-gradient(circle at 55% 40%, #f4f4f6 0%, #d2d8e2 40%, #3a8fd8 100%); }

  .intro { position: absolute; left: 637px; top: 40px; width: 260px; font-size: 15.6px; line-height: 17.4px; color: var(--navy); font-family: "Oswald", "Arial Narrow", sans-serif; font-weight: 600; }

  .checklist { position: absolute; left: 636px; top: 106px; list-style: none; }
  .checklist li { position: relative; padding-left: 20px; font-size: 11px; line-height: 13.5px; font-weight: 700; color: var(--ink-soft); margin-bottom: 4px; }
  .checklist li svg { position: absolute; left: 1px; top: 2px; width: 9px; height: 9px; }

  .feature { position: absolute; left: 636px; font-family: "Oswald", "Arial Narrow", sans-serif; font-weight: 700; font-size: 14px; line-height: 17.4px; text-transform: uppercase; color: var(--ink-soft); }
  .feature .accent { color: var(--navy); display: block; }
  .feature.grades { top: 219px; }
  .feature.family { top: 273px; }
  .feature.safety { top: 325px; color: var(--navy); }

  .age-list { position: absolute; left: 636px; top: 388px; width: 290px; list-style: none; font-size: 10.6px; line-height: 13.6px; color: var(--ink-soft); }
  .age-list li { margin-bottom: 3.8px; }
  .age-list strong { font-weight: 700; }

  .band { position: absolute; left: 0; top: 0; width: 959px; height: 678px; }

  .band-text { position: absolute; right: 530px; top: 604px; text-align: right; font-size: 16.5px; line-height: 19.6px; color: #ffffff; letter-spacing: 0.3px; }

  .photo-team { left: 619px; top: 548px; width: 310px; height: 130px; background: linear-gradient(180deg, #5d626c 0%, #8a8f99 40%, #e9e9ec 75%, #cfd2d8 100%); }
</style>
</head>
<body>
  <main class="spread">
    <div class="photo photo-founder" role="img" aria-label="Cut-out photo of the school founder in a white karate gi and black belt, holding training weapons"></div>

    <h1 class="main-title heading-font">Why Choose<br>Kaminari?</h1>

    <section class="reason known">
      <h3>Well Known</h3>
      <p>We are Dunmore’s most popular martial arts school. Kaminari has a massive social media following right around the world. We regularly have instructors from Japan visiting our dojo.</p>
    </section>
    <section class="reason equipped">
      <h3>Well Equipped</h3>
      <p>We have the largest and best equipped martial arts school in Australia. In fact, it is the best we have seen anywhere in the world.</p>
    </section>
    <section class="reason versed">
      <h3>Well Versed</h3>
      <p>We offer internationally recognised grades from some of the most prestigious and respected budo associations in the world. All of our black belt grades are registered in Japan.</p>
    </section>
    <section class="reason experienced">
      <h3>Well Experienced</h3>
      <p>The founder of Kaminari, Sensei Glen, has been training since 1987 and has well over 15000 hours of teaching experience behind him and has been awarded black belts in 9 different styles.</p>
    </section>

    <div class="photo photo-thumb sparring" role="img" aria-label="Photo of students sparring with headgear near a boxing ring"></div>
    <div class="photo photo-thumb weapons" role="img" aria-label="Photo of two students practising weapons on blue mats"></div>
    <div class="photo photo-thumb grading" role="img" aria-label="Photo of three students in gis holding grading certificates"></div>

    <p class="intro">We have a comprehensive Stand Tall program that has been helping kids for well over a decade.</p>

    <ul class="checklist">
      <li><svg viewBox="0 0 10 10"><path d="M1 5.5 L4 8.5 L9 1" fill="none" stroke="#3a3a3a" stroke-width="1.2"/></svg>Choose from 80 classes a week.</li>
      <li><svg viewBox="0 0 10 10"><path d="M1 5.5 L4 8.5 L9 1" fill="none" stroke="#3a3a3a" stroke-width="1.2"/></svg>QR code to my website timetable</li>
      <li><svg viewBox="0 0 10 10"><path d="M1 5.5 L4 8.5 L9 1" fill="none" stroke="#3a3a3a" stroke-width="1.2"/></svg>Try a FREE lesson and receive a FREE uniform.<br>&nbsp;Save up to $161.99</li>
      <li><svg viewBox="0 0 10 10"><path d="M1 5.5 L4 8.5 L9 1" fill="none" stroke="#3a3a3a" stroke-width="1.2"/></svg>You don’t have to be great to start</li>
    </ul>

    <div class="photo photo-circle" role="img" aria-label="Circular photo of kids in white gis on blue mats practising a ground technique"></div>

    <p class="feature grades"><span class="accent">Internationally</span>Recognised Grades</p>
    <p class="feature family"><span class="accent">Family Friendly</span>Safe Environment</p>
    <p class="feature safety">To keep our members<br>safe we have strict<br>age restrictions.</p>

    <ul class="age-list">
      <li><strong>Karate for Toddlers</strong> – 2 to 4 year old’s</li>
      <li><strong>Kids Karate, Kids Muay Thai,<br>Kids Kick Boxing</strong> – 3 to 7 year old’s</li>
      <li><strong>Kids Boxing</strong> – 6 to 11 years</li>
      <li><strong>Boxing</strong> – 11 years up to adults</li>
      <li><strong>Karate Self Defence, Muay Thai Kick Boxing,<br>Weapons</strong> - 7 years up to adults</li>
      <li><strong>Kids BJJ</strong> – 6 to 13 years</li>
      <li><strong>BJJ</strong> - 13 years up to adults</li>
    </ul>

    <svg class="band" viewBox="0 0 959 678" aria-hidden="true">
      <path fill="var(--band)" d="M0 586 C 240 560, 620 548, 959 566 L959 678 L0 678 Z"/>
    </svg>

    <div class="photo photo-team" role="img" aria-label="Group photo of instructors and students in white gis with coloured belts inside the dojo"></div>

    <p class="band-text heading-font">Over 80 classes a week to choose<br>from classes 6 days a week</p>
  </main>
</body>
</html>
```